Banner Ad Design Project: rolverantco.com

Google all ad dimensions banner pack for http://www.rolverantco.com.

Ad dimensions Max. file sizes (KB) Ad types
468 × 60 50 Banner
728 × 90 50 Leaderboard
250 × 250 50 Square
200 × 200 50 Small square
336 × 280 50 Large rectangle
300 × 250 50 Inline rectangle
120 × 600 50 Skyscraper
160 × 600 50 Wide skyscraper
300 × 600 200 Half-page ad
970 × 90 200 Large leaderboard
240 × 400 50 Vertical rectangle
980 × 120 200 Panorama
930 × 180 200 Top banner
250 × 360 50 Triple widescreen
580 × 400 200 Netboard

*Please visit the website and come up with unique ideas.

Target Market(s)

Consumers looking to transport a car, motor vehicle, motorcycle or anything that has wheels and a motor in the united states long distance.

Industry/Entity Type

Google

Requirements
Must have
• a call to action for example (RANDOM ONE):
-
TALK TO A REAL CAR SHIPPING PRO NOW: 1-888-614-2753
HAVE CAR TRANSPORT QUESTIONS? CALL NOW: 1-888-614-2753
CALL NOW & TALK TO A REAL AUTO SHIPPING EXPERT: 1-888-614-2753
Call Now Free Quote:1-888-614-2753

Nice to have
• Best Value For Dollar Auto Transport
Bonded, Insured & Licensed
Price Match Guarantee: will match any price by a 4 or 5 star rated Company.
Best of all, you pay nothing until your car is picked up!
Nationwide Door-To-Door Vehicle Shipping
Should not have
• Logo integrated in to the design.
bold call to action; ex; call now free quote:
Heading style phone number, 888-614-2753, stands out and screams call now.
example:
CALL ROLVERANT TODAY TO TRANSPORT YOUR VEHICLE
1-888-614-2753

```html
<!DOCTYPE html>
<html lang="en">
<head>
<meta charset="utf-8">
<title>Rolverant – Car Transport Questions Banner</title>
<link href="https://fonts.googleapis.com/css2?family=Oswald:wght@500;600;700&display=swap" rel="stylesheet">
<style>
  :root {
    --bg: #ffffff;
    --navy-text: #2c3e5c;
    --orange: #f05a1a;
    --panel-dark: #243650;
    --panel-light: #4b6382;
    --white: #ffffff;
    --photo-light: #f3e6d6;
    --photo-mid: #d9b98c;
    --photo-dark: #b8c9dc;
  }
  * { margin: 0; padding: 0; box-sizing: border-box; }
  html, body {
    width: 1200px;
    height: 148px;
    overflow: hidden;
    background: var(--bg);
  }
  .banner {
    position: relative;
    width: 1200px;
    height: 148px;
    background: var(--bg);
    font-family: "Oswald", "Arial Narrow", sans-serif;
    overflow: hidden;
  }
  .agent-photo {
    position: absolute;
    left: 0;
    top: 0;
    width: 232px;
    height: 148px;
    background: linear-gradient(90deg, var(--photo-mid) 0%, var(--photo-light) 45%, var(--photo-dark) 80%, var(--bg) 100%);
  }
  .headline {
    position: absolute;
    left: 326px;
    top: 6px;
    text-transform: uppercase;
    line-height: 1;
  }
  .headline-lead {
    display: block;
    color: var(--navy-text);
    font-weight: 600;
    font-size: 49px;
    letter-spacing: 0.2px;
  }
  .headline-main {
    display: block;
    color: var(--orange);
    font-weight: 600;
    font-size: 84px;
    letter-spacing: 0.5px;
    margin-top: -4px;
  }
  .call-panel {
    position: absolute;
    left: 844px;
    top: 0;
    width: 356px;
    height: 148px;
    background: linear-gradient(180deg, var(--panel-light) 0%, var(--panel-dark) 100%);
  }
  .call-panel-notch {
    position: absolute;
    left: 0;
    top: 46px;
  }
  .call-label {
    position: absolute;
    left: 38px;
    top: 26px;
    color: var(--white);
    font-weight: 500;
    font-size: 40px;
    line-height: 1;
    text-transform: uppercase;
  }
  .call-number {
    position: absolute;
    left: 38px;
    top: 76px;
    color: var(--white);
    font-weight: 500;
    font-size: 50px;
    line-height: 1;
    letter-spacing: -0.5px;
  }
</style>
</head>
<body>
  <div class="banner">
    <div class="agent-photo" role="img" aria-label="Smiling customer service agent wearing a headset"></div>

    <h1 class="headline">
      <span class="headline-lead">Have car transport</span>
      <span class="headline-main">Questions?</span>
    </h1>

    <div class="call-panel">
      <svg class="call-panel-notch" width="14" height="28" viewBox="0 0 14 28" aria-hidden="true">
        <polygon points="0,0 14,14 0,28" fill="#ffffff"/>
      </svg>
      <div class="call-label">Call now</div>
      <div class="call-number">1-888-614-2753</div>
    </div>
  </div>
</body>
</html>
```